Wirenexa

I'm looking to much improve our current website wirenexa.com
Updates

Low design quality

Target Market(s)

Commercial clients (Not-Residentials)

Industry/Entity Type

Office buildings and Industrial clients

Coding

Coded - Design and coding required

Number of Pages Required

5+ page

Requirements
Must have
• Very professional structured low voltage cabling projects for Wi-Fi, Audio/Video conference rooms, Access Control systems, CCTV.

```html
<!DOCTYPE html>
<html lang="en">
<head>
<meta charset="utf-8">
<title>Wirenexa – Low Voltage Cabling</title>
<link href="https://fonts.googleapis.com/css2?family=Figtree:wght@400;500;600;700;800&display=swap" rel="stylesheet">
<style>
:root{
  --red:#e0342f;
  --ink:#1d1d1f;
  --text:#333;
  --muted:#8a8a8a;
  --line:#d9d9d9;
  --card:#f4f4f4;
  --white:#fff;
  --hero-dark:#1b1b1d;
  --diagram-tint:#f3f3f3;
}
*{box-sizing:border-box;margin:0;padding:0}
html,body{width:1200px;height:1200px;overflow:hidden;background:var(--white);font-family:"Figtree",sans-serif;color:var(--text)}
body{position:relative}
.site-header{position:absolute;top:0;left:0;width:1200px;height:76px;display:flex;align-items:center;justify-content:space-between;padding:0 60px 0 59px;background:var(--white)}
.brand{display:flex;align-items:center;gap:8px;font-size:27px;font-weight:800;color:var(--ink);letter-spacing:-.5px}
.brand-mark{width:32px;height:32px;background:var(--red);border-radius:3px}
.main-nav{display:flex;align-items:center;gap:28px;font-size:14px}
.main-nav a{color:var(--text);text-decoration:none}
.main-nav a.active{color:var(--red);font-weight:500}
.main-nav .nav-phone{color:var(--red);font-weight:700;font-size:15px}
.hero{position:absolute;top:75px;left:0;width:1200px;height:610px;overflow:hidden}
.hero-photo{position:absolute;inset:0;background:radial-gradient(ellipse at 40% 20%,#3a3a30 0%,#262624 35%,var(--hero-dark) 70%),linear-gradient(90deg,#1e1e1e,#2a201f)}
.hero-copy{position:absolute;left:60px;top:146px;width:600px;color:var(--white)}
.hero-copy h1{font-size:41px;line-height:47px;font-weight:800;letter-spacing:-1px}
.hero-copy p{margin-top:17px;font-size:18px;color:#cfcfcf}
.callback-card{position:absolute;left:695px;top:38px;width:445px;height:472px;background:var(--card);border-radius:18px;padding:46px 36px 0}
.callback-card h2{font-size:23px;font-weight:800;color:var(--ink);letter-spacing:-.3px}
.callback-card .lead{margin-top:16px;font-size:13px;color:#444}
.callback-form{margin-top:24px;display:flex;flex-direction:column;gap:17px}
.field{height:35px;width:374px;background:var(--white);border:1px solid var(--line);border-radius:7px;padding:0 13px;display:flex;align-items:center;font-size:14px;color:var(--muted)}
.field.textarea{height:79px;align-items:flex-start;padding-top:12px}
.submit-btn{margin-top:3px;width:154px;height:42px;border:none;border-radius:8px;background:var(--red);color:var(--white);font-family:inherit;font-weight:700;font-size:14px;box-shadow:0 6px 14px rgba(224,52,47,.35)}
.services-diagram{position:absolute;top:770px;left:20px;width:1160px;height:220px;border-radius:12px;background:linear-gradient(180deg,var(--white) 0%,var(--diagram-tint) 50%,var(--white) 100%)}
.intro-heading{position:absolute;top:1106px;left:0;width:1200px;text-align:center;font-size:33px;line-height:44px;font-weight:800;color:var(--ink);letter-spacing:-.8px;padding:0 90px}
</style>
</head>
<body>
<header class="site-header">
  <div class="brand"><span class="brand-mark"></span>Wirenexa</div>
  <nav class="main-nav">
    <a class="active" href="#">Home</a>
    <a href="#">About Us</a>
    <a href="#">Services</a>
    <a href="#">Contact</a>
    <a class="nav-phone" href="#">(888) 555-0147</a>
  </nav>
</header>

<section class="hero">
  <div class="hero-photo" role="img" aria-label="Dark server rack with network patch cables"></div>
  <div class="hero-copy">
    <h1>Professional Cabling for Computers, Security Cameras, Wi-Fi, VOIP Phones, Access Control, Video and Audio.</h1>
    <p>Virginia, Washington DC, Maryland</p>
  </div>
  <div class="callback-card">
    <h2>Request Callback</h2>
    <p class="lead">Submit the form and we will contact you within 1 hour.</p>
    <form class="callback-form">
      <div class="field">Name</div>
      <div class="field">Email *</div>
      <div class="field">Phone</div>
      <div class="field textarea">Message or Request *</div>
      <button class="submit-btn" type="button">Submit Request</button>
    </form>
  </div>
</section>

<div class="services-diagram" role="img" aria-label="Illustration of intertwined cables linking the services: Security Cameras, Wi-Fi, Video and Audio, Computers, VOIP Phones and Access Control"></div>

<h2 class="intro-heading">Elevate Your Connectivity with Wirenexa's Low Voltage Cabling Solutions</h2>
</body>
</html>
```